Tenlo business card

I'm a hack at Illustrator, but have put together a set of business cards as attached. If someone could please improve these including good font selection, standard font sizes and spacing, nice layout and symmetry. Rear side the same on all cards. Basically make these cards into something impressive and professional.
Updates

Official logo just uploaded, please use these colours

Target Market(s)

50+ year old married couples

Industry/Entity Type

Business

Requirements
Must have
• Professional
Should not have
• Silly, cartoony

```html
<!DOCTYPE html>
<html lang="en">
<head>
<meta charset="utf-8">
<title>Tenlo business card</title>
<link rel="stylesheet" href="https://fonts.googleapis.com/css2?family=Noto+Sans:wght@400;600;700&family=Dosis:wght@300;500;600;700&family=Cabin:wght@400;500&display=swap">
<style>
  :root {
    --page: #ffffff;
    --card: #1159a0;
    --card-light: #0f62aa;
    --card-dark: #174a8a;
    --ink: #ffffff;
    --ink-soft: #c9d4e2;
    --accent: #72c3f2;
  }
  * { margin: 0; padding: 0; box-sizing: border-box; }
  html, body { width: 1200px; height: 1000px; overflow: hidden; background: var(--page); }
  .canvas { position: relative; width: 1200px; height: 1000px; }

  .card {
    position: absolute; top: 130px; width: 463px; height: 738px;
    background: var(--card); overflow: hidden; color: var(--ink);
    box-shadow: 0 2px 6px rgba(0,0,0,.12);
  }
  .card--front { left: 120px; border-radius: 70px 0 70px 0; }
  .card--back  { left: 618px; border-radius: 0 70px 0 70px; }
  .card__shade { position: absolute; inset: 0; width: 100%; height: 100%; }

  .line { position: absolute; white-space: nowrap; line-height: 1; }
  .center { left: 0; right: 0; text-align: center; }

  /* front */
  .brand { position: absolute; left: 0; right: 0; top: 52px; display: flex; flex-direction: column; align-items: center; gap: 22px; }
  .brand__mark { width: 38px; height: 38px; background: var(--ink); border-radius: 4px; }
  .brand__name { font-family: "Noto Sans", sans-serif; font-weight: 700; font-size: 34px; letter-spacing: 18px; margin-right: -18px; color: var(--ink); line-height: 1; }

  .person__name { top: 268px; font-family: "Noto Sans", sans-serif; font-weight: 700; font-size: 31px; color: var(--accent); }
  .person__role { top: 316px; font-family: "Noto Sans", sans-serif; font-weight: 600; font-size: 23px; }
  .person__tag  { top: 354px; font-family: "Noto Sans", sans-serif; font-size: 16px; color: var(--ink-soft); }
  .contact { font-family: "Noto Sans", sans-serif; font-weight: 700; font-size: 19px; }
  .contact--mobile { top: 458px; }
  .contact--direct { top: 483px; }
  .contact--email  { top: 535px; }
  .website { top: 675px; font-family: "Cabin", sans-serif; font-size: 22px; letter-spacing: 3px; }

  /* back */
  .service { font-family: "Dosis", sans-serif; font-weight: 600; }
  .service--lead  { top: 116px; left: 87px; font-size: 30px; }
  .service--solar { top: 159px; left: 89px; font-size: 16px; font-weight: 700; }
  .service--led   { top: 186px; left: 73px; font-size: 35px; font-weight: 500; }
  .service--led .light { font-weight: 300; }
  .service--heat  { top: 235px; left: 62px; font-size: 16px; font-weight: 700; }
  .service--pcm   { top: 262px; left: 115px; font-size: 23px; font-weight: 500; }
  .service--air   { top: 303px; left: 61px; font-size: 16px; font-weight: 700; }
  .service--auto  { top: 328px; left: 63px; font-size: 27px; font-weight: 500; }

  .address { position: absolute; right: 44px; top: 583px; text-align: right; font-family: "Cabin", sans-serif; font-size: 17px; letter-spacing: 1px; line-height: 25px; }
  .registration { top: 680px; left: 88px; font-family: "Cabin", sans-serif; font-size: 17px; letter-spacing: .5px; }
</style>
</head>
<body>
<main class="canvas">

  <section class="card card--front" aria-label="Card front">
    <svg class="card__shade" viewBox="0 0 463 738" preserveAspectRatio="none" aria-hidden="true">
      <circle cx="560" cy="430" r="520" fill="var(--card-light)"/>
      <path d="M0 575 Q230 560 463 590 L463 738 L0 738 Z" fill="var(--card-dark)" opacity=".75"/>
      <circle cx="-160" cy="380" r="430" fill="none" stroke="var(--card-dark)" stroke-width="2" opacity=".4"/>
    </svg>

    <div class="brand">
      <span class="brand__mark" aria-hidden="true"></span>
      <span class="brand__name">TENLO</span>
    </div>

    <div class="line center person__name">Mark Ellison</div>
    <div class="line center person__role">General Manager</div>
    <div class="line center person__tag">Building &amp; Technology Innovator</div>

    <div class="line center contact contact--mobile">M : 0400 555 123</div>
    <div class="line center contact contact--direct">D : 03 9000 1099</div>
    <div class="line center contact contact--email">mark.ellison@tenlo.com.au</div>

    <div class="line center website">www.tenlo.com.au</div>
  </section>

  <section class="card card--back" aria-label="Card back">
    <svg class="card__shade" viewBox="0 0 463 738" preserveAspectRatio="none" aria-hidden="true">
      <circle cx="-80" cy="330" r="470" fill="var(--card-light)"/>
      <path d="M0 575 Q230 560 463 575 L463 738 L0 738 Z" fill="var(--card-dark)" opacity=".75"/>
      <circle cx="620" cy="300" r="480" fill="none" stroke="var(--card-dark)" stroke-width="2" opacity=".4"/>
    </svg>

    <div class="line service service--lead">Building design &amp; constuction</div>
    <div class="line service service--solar">Hybrid, On &amp; Off grid Solar Power Systems</div>
    <div class="line service service--led">LED Lighting, <span class="light">Insulation</span></div>
    <div class="line service service--heat">Heat Pumps for pools, hyrdronics &amp; hot water</div>
    <div class="line service service--pcm">Phase Change Material (PCM)</div>
    <div class="line service service--air">Fresh air ventilation with air to air heat exchangers</div>
    <div class="line service service--auto">Automation, Air conditioning</div>

    <address class="address" style="font-style:normal">
      8/41 Harbour St<br>
      Elmsford, VIC 3199, Australia<br>
      Ph: (+61) 03 9000 1050
    </address>
    <div class="line registration">REC 40718&nbsp;&nbsp;&nbsp;ABN XXXXXXXXXXXXX</div>
  </section>

</main>
</body>
</html>
```